Facial Cosmetic Business Card Design

I am a Physician certified in Lumivex injections, Sorelane fillers,& Chemical Peels.
I do no surgery
I have 20 years experience in facial cosmetics
30+ years medical experience
name is not TM but thought something like "Radiant Visage" catches what I do and the look I get with minimal to no downtime and no recovery time.
I do home parties and also private home consultations and treatments in a relaxed atmosphere with no pressure.
Aestheology services upon referral to a private associate as well.
I have no logo, photo's or desigs so I am ope to suggestions

To all the MD is my medical degree

the MNGGC are my board certifications stands for Member National Guild General Care
4816 Cedar Hollow Lane is my office home address
4045518832 is my cell/office number or contact info

Thanks

Reason: Sorry was out of town I like a few of the designs so I have enough to choose from set tweeks to be done with prof degree and address mixup. Once i see corrections I will choose approp one thanks all Dr Kessler

Target Market(s)

mostly wome do these procedures usually i the above 35 crowd certainly over 40 crowd for sure

Industry/Entity Type

Medical

Contact Information for Business Card

Radiant Visage, Daniel Kessler MD, MNGGC
4816 Cedar Hollow Lane
Suwanee, Ga. 30024
O:404-551-9016
C:404-551-8832
F:404-551-9070

```html
<!DOCTYPE html>
<html lang="en">
<head>
<meta charset="utf-8">
<title>Radiant Visage – Business Card Options</title>
<link rel="stylesheet" href="https://fonts.googleapis.com/css2?family=Mulish:wght@400;700;800&display=swap">
<style>
  :root {
    --frame: #3a80f2;
    --royal: #2a7fff;
    --aqua: #00ffff;
    --white: #ffffff;
    --swirl: #dff8fb;
  }
  * { margin: 0; padding: 0; box-sizing: border-box; }
  html, body { width: 1200px; height: 929px; overflow: hidden; background: var(--white); }
  .sheet {
    position: relative;
    width: 1200px;
    height: 929px;
    border: 2px solid var(--frame);
    font-family: "Mulish", "Century Gothic", sans-serif;
  }
  .card {
    position: absolute;
    top: 278px;
    width: 557px;
    height: 343px;
    border: 2px solid var(--frame);
    background: var(--white);
    overflow: hidden;
  }
  .card--royal { left: 24px; --accent: var(--royal); }
  .card--aqua  { left: 615px; --accent: var(--aqua); }
  .card__art { position: absolute; inset: 0; width: 100%; height: 100%; }
  .card__wave { fill: var(--accent); }
  .doctor-name {
    position: absolute;
    right: 91px;
    top: 27px;
    font-size: 20px;
    font-weight: 700;
    letter-spacing: -0.2px;
    color: var(--accent);
  }
  .practice {
    position: absolute;
    left: 14px;
    top: 172px;
    color: var(--accent);
  }
  .practice__name {
    font-size: 19px;
    font-weight: 800;
    letter-spacing: 0.2px;
    margin-bottom: 6px;
  }
  .practice__address {
    font-size: 15px;
    line-height: 22px;
    font-style: normal;
  }
  .contact {
    position: absolute;
    left: 413px;
    top: 256px;
    list-style: none;
    color: var(--white);
    font-size: 14.5px;
    font-weight: 700;
    line-height: 22.5px;
  }
</style>
</head>
<body>
<main class="sheet">

  <section class="card card--royal">
    <svg class="card__art" viewBox="0 0 419 258" preserveAspectRatio="none">
      <defs>
        <radialGradient id="swirl-royal" cx="50%" cy="50%" r="50%">
          <stop offset="0%" stop-color="var(--swirl)" stop-opacity="0.15"/>
          <stop offset="70%" stop-color="var(--swirl)" stop-opacity="0.7"/>
          <stop offset="100%" stop-color="var(--swirl)" stop-opacity="0"/>
        </radialGradient>
      </defs>
      <ellipse role="img" aria-label="Decorative flowing script initial" cx="215" cy="135" rx="200" ry="120" fill="url(#swirl-royal)"/>
      <path class="card__wave" d="M0 258 L0 255 C60 252 130 252 180 240 C250 220 270 130 320 80 C350 50 385 25 419 8 L419 258 Z"/>
    </svg>
    <h1 class="doctor-name">Daniel Kessler MD</h1>
    <div class="practice">
      <h2 class="practice__name">RADIANT VISAGE</h2>
      <address class="practice__address">MNGGC 4816 Cedar Hollow Lane Brookfield,<br>Ga 30158</address>
    </div>
    <ul class="contact">
      <li>O:404-551-9016</li>
      <li>C:404-551-8832</li>
      <li>F:404-551-9070</li>
    </ul>
  </section>

  <section class="card card--aqua">
    <svg class="card__art" viewBox="0 0 419 258" preserveAspectRatio="none">
      <defs>
        <radialGradient id="swirl-aqua" cx="50%" cy="50%" r="50%">
          <stop offset="0%" stop-color="var(--swirl)" stop-opacity="0.15"/>
          <stop offset="70%" stop-color="var(--swirl)" stop-opacity="0.7"/>
          <stop offset="100%" stop-color="var(--swirl)" stop-opacity="0"/>
        </radialGradient>
      </defs>
      <ellipse role="img" aria-label="Decorative flowing script initial" cx="215" cy="135" rx="200" ry="120" fill="url(#swirl-aqua)"/>
      <path class="card__wave" d="M0 258 L0 255 C60 252 130 252 180 240 C250 220 270 130 320 80 C350 50 385 25 419 8 L419 258 Z"/>
    </svg>
    <h1 class="doctor-name">Daniel Kessler MD</h1>
    <div class="practice">
      <h2 class="practice__name">RADIANT VISAGE</h2>
      <address class="practice__address">MNGGC 4816 Cedar Hollow Lane Brookfield,<br>Ga 30158</address>
    </div>
    <ul class="contact">
      <li>O:404-551-9016</li>
      <li>C:404-551-8832</li>
      <li>F:404-551-9070</li>
    </ul>
  </section>

</main>
</body>
</html>
```